DeskHarbor | A Brightday Company

We need to Develop a Sales Brochure for a coworking space:
1. About DeskHarbor
2. Location
3. Cards to Show Benefits
4. Floor Plan and Pictures
5. Pricing Card

Jersey City Coworking/Shared Office Space, Steps from Linden LINK
Impress your clients. Stimulate your creativity. Unleash your inner genius.
DeskHarbor is Jersey City’s newest premier coworking and shared office space,

home to:

 Entrepreneurs
 Visionaries
 Freelancers
 Consultants
 Telecommuters
 Startups
 + More

Here you’ll have access to everything you need in order to work efficiently, productively, happily and healthily. Essentials, Amenities and Resources
 Furnished office space with 24/7 access
 Conference rooms and meeting spaces
 Networking events and educational workshops
 Business support
 Ultra-High Speed Internet
 Secure WiFi
 Print + Copy + Scan
 Mail service and business address
 White boards and office supplies
 Gourmet teas and coffees
 Kitchen stocked with healthy snacks
 + More

Member Discounts
 Hotel
 Travel
 Car Rental
 Cloud and server
 + More

Our Values

Collaboration, Community, Happiness, Wellness, Growth
Bonus: Our short-term funding program offers financial support to help your business reach its next milestone.
Location and Pricing
DeskHarbor is located at 482 Marlow Court Lane in Jersey City, a prestigious
address on the banks of the Hudson River, just minutes from the Brevard Tunnel and steps from the Linden LINK station.
1. The cover of the brochure should create excitement to open the folder. Do not create a trifold. We are a very high end office space not a medical office. The size of the paper, does not have to be standard. Think card stock, matt or Glossy or Both

2. On Opening the Brochure - The First Page is to educate my client with a art, color and words
3. Page 2,3,4 and 5Is about Inspiration and explanation: I am thinking that they should be cards of detail:
1. Orange: Vision - Consider a theme of Innovation, High Performance, Fun, Value from action, resources, impulse
2. Gold: Details: Orange: Vision - Consider a theme of Authority and Leadership. The duty to Shine, the leader being the backbone of the group. Practial, values of home, status, security, and traditions
3. Blue: Encourage and support, A peacemaker, Think about themes of caring, counseling, nurturing, Idealistic and sympathetic. This is about contribution
4. Green: The Independent thinker, seeking knowledge, intelligence, justice and insight. About the details

The message on these cards should be similar but at various levels of detail

The 5th Card is about Floor Plans - You are not responsible for it this card. Just the Look of how the card should look like

The 6th Card is about pricing
Updates

Project Deadline Extended
Reason: Only 1 designer has provided a decent design. Most of the submissions were recycled and not in line. Please extend by 4 weeks.

Target Market(s)

- Technology Companies (10 people or less)
- Entrepreneurs (2 People)
- Freelancers (1 People)
- small size Technology Company (5 people or less)

Industry/Entity Type

It Company

Font styles to use
Other font styles liked:
• Caviar Dreams and Sans Serif

Requirements
Must have
• - Pictures
• - Details
• - Inspiration
• - FLoor plans
• - Questions and Value
• - Minimal
• Why would they want to buy your product? 
• What's the most important thing it can do for them?
• What is the most important problem your product or service can solve for them?
• To be effective, your brochure needs to get attention, get the prospect interested enough to read further, raise their desire for the product or service, and get them to take a specific action such as buy now, call and make an appointment, return a post card.
Nice to have
• I am open to design - be inspirational
• Should be clear
• They are interested in themselves and/or their own businesses. To get their attention, your brochure needs to focus on the benefits they will enjoy by making a purchase from you.
Should not have
• Cannot be too Salesy
• No Stock pictures
• Don't put a picture of your building on the cover of the brochure
• The only thing they care about is whether or not your products meet their needs.

```html
<!DOCTYPE html>
<html lang="en">
<head>
<meta charset="utf-8">
<title>DeskHarbor Brochure Cards</title>
<link rel="stylesheet" href="https://fonts.googleapis.com/css2?family=Source+Sans+3:wght@300&display=swap">
<style>
  :root {
    --bg: #c9c9c9;
    --orange: #f37039;
    --gold: #efcb27;
    --blue: #4f95d1;
    --green: #8dc341;
    --ink: #ffffff;
    --numeral: rgba(255, 255, 255, 0.2);
    --fold-shade: rgba(0, 0, 0, 0.06);
  }
  * { margin: 0; padding: 0; box-sizing: border-box; }
  html, body {
    width: 1200px;
    height: 1168px;
    overflow: hidden;
    background: var(--bg);
    font-family: "Source Sans 3", sans-serif;
    font-weight: 300;
    color: var(--ink);
  }
  .spread {
    position: absolute;
    left: 117px;
    width: 961px;
    height: 481px;
    display: flex;
    box-shadow: 0 2px 4px rgba(0, 0, 0, 0.35);
  }
  .spread--top { top: 70px; }
  .spread--bottom { top: 585px; }
  .card {
    position: relative;
    width: 50%;
    height: 100%;
    overflow: hidden;
  }
  .card--orange { background: var(--orange); }
  .card--gold { background: var(--gold); }
  .card--blue { background: var(--blue); }
  .card--green { background: var(--green); }
  .card--left::after {
    content: "";
    position: absolute;
    top: 0; right: 0;
    width: 40px; height: 100%;
    background: linear-gradient(to right, transparent, var(--fold-shade));
  }
  .numeral {
    position: absolute;
    color: var(--numeral);
    line-height: 1;
    font-weight: 300;
  }
  .card-copy {
    position: absolute;
    font-size: 19px;
    line-height: 18.4px;
    letter-spacing: -0.2px;
  }
  .card--orange .numeral { left: -20px; top: -52px; font-size: 290px; }
  .card--orange .card-copy { left: 42px; top: 45px; width: 200px; }

  .card--gold .numeral { left: 355px; top: 265px; font-size: 290px; }
  .card--gold .card-copy { left: 39px; top: 351px; width: 420px; }

  .card--blue .numeral { left: -70px; top: 205px; font-size: 290px; }
  .card--blue .card-copy { left: 38px; top: 361px; width: 320px; font-size: 17px; }

  .card--green .numeral { left: 140px; top: -48px; font-size: 280px; }
  .card--green .card-copy {
    left: 290px; top: 40px; width: 180px;
    font-size: 28px; line-height: 25.6px;
  }
</style>
</head>
<body>
  <section class="spread spread--top">
    <article class="card card--orange card--left">
      <span class="numeral">1</span>
      <p class="card-copy">Vision - Consider a theme of Innovation, High Performance, Fun, Value from action, resources, impulse</p>
    </article>
    <article class="card card--gold">
      <span class="numeral">2</span>
      <p class="card-copy">Vision - Consider a theme of Authority and Leadership. The duty to Shine, the leader being the backbone of the group. Practial, values of home, status, security, and traditions</p>
    </article>
  </section>

  <section class="spread spread--bottom">
    <article class="card card--blue card--left">
      <span class="numeral">3</span>
      <p class="card-copy">Encourage and support, A peacemaker, Think about themes of caring, counseling, nurturing, Idealistic and sympathetic. This is about contribution</p>
    </article>
    <article class="card card--green">
      <span class="numeral">4</span>
      <p class="card-copy">The Independent thinker, seeking knowledge, intelligence, justice and insight. About the details</p>
    </article>
  </section>
</body>
</html>
```